Room Hire at The Willowmere Talking Rooms House to encourage therapists to hire rooms from us

An A4 page for magazine printing and use to send online as well.

We want to attract therapists to come and hire our beautiful rooms. We have a soft green, cream and brown colour theme and a professional, warm, elegant style (we hope)
I've uploaded the previous advert we had done through brief bazaar which was aimed at attracting therapy clients.

Target Market(s)

psychotherapists and physical therapists searching to hire consulting rooms

Industry/Entity Type

Printing

Font styles to use
Serif
Sans Serif
Script
Other font styles liked:
• Good Vibes

Colors
cadf82
abd037
9bcb3c
fdf9ce
fff3d1

Requirements
Must have
• Please include this text
• Website address
• rooms@hwrk-ashlake.co.uk address
• "The rooms are available to hire all day into the evenings and at weekends.
• There are 8 rooms, all suitable for Couples work, Individual Counselling or Supervision sessions. Some rooms are designed to be used by physical therapists as well. One of them is large enough to use for Family Therapy, to hold groups or to run Training Sessions for approximately fourteen people."
• The colour scheme to harmonise with our website theme colours and fonts - Colour RGA numbers
• Brown
• Red 65
• Green 53
• Blue 53
• Light green
• Red 129
• Green 157
• Blue 115
• www.hwrk-ashlake.co.uk.
• Scrolling writing is Good Vibes by Google
• Be warm, calm, welcoming, professional styling, striking.
Nice to have
• Pictures of our rooms if we can provide enough quality for printing
Should not have
• Pictures of people touching each other.
• Not be too busy or angular

```html
<!DOCTYPE html>
<html lang="en">
<head>
<meta charset="utf-8">
<title>Room Hire – The Willowmere Talking Rooms House</title>
<link href="https://fonts.googleapis.com/css2?family=Great+Vibes&family=Open+Sans:wght@400;600;700&display=swap" rel="stylesheet">
<style>
  :root {
    --brown: #413535;
    --cream: #fdf6d0;
    --mint: #e4efd0;
    --leaf-green: #1f9a4a;
    --lime: #9bcb3c;
    --white: #ffffff;
  }
  html, body { margin: 0; padding: 0; overflow: hidden; background: #f2f2f2; }
  .page {
    position: relative;
    width: 848px; height: 1200px;
    overflow: hidden;
    background: var(--mint);
    font-family: "Open Sans", Arial, sans-serif;
    color: var(--brown);
  }
  .backdrop { position: absolute; inset: 0; }
  .brand {
    position: absolute; left: 18px; top: 236px;
    transform: rotate(-21deg); transform-origin: left bottom;
    display: flex; align-items: center; gap: 10px;
    font-family: "Great Vibes", "Good Vibes", cursive;
    font-size: 38px; line-height: 1.1; color: var(--brown); white-space: nowrap;
  }
  .brand-dot { width: 14px; height: 14px; border-radius: 50%; background: var(--lime); flex: none; }
  .script {
    position: absolute; margin: 0; font-weight: 400;
    font-family: "Great Vibes", "Good Vibes", cursive;
    line-height: 1; white-space: nowrap;
  }
  .script--lead { left: 140px; top: 340px; font-size: 62px; color: var(--leaf-green); }
  .script--hero { left: 70px; top: 400px; font-size: 140px; color: var(--brown); }
  .script--sub { left: 78px; top: 522px; font-size: 52px; color: var(--leaf-green); }
  .script--hero2 { left: 80px; top: 560px; font-size: 140px; color: var(--brown); }
  .side-bar { position: absolute; left: 0; top: 690px; width: 40px; height: 270px; background: var(--brown); }
  .rooms-copy {
    position: absolute; left: 66px; top: 694px; width: 300px;
    font-size: 14px; line-height: 1.3;
  }
  .rooms-copy p { margin: 0; }
  .rooms-copy strong { font-weight: 700; font-size: 20px; line-height: 1.1; }
  .rooms-copy .detail { width: 262px; }
  .hours {
    position: absolute; left: 20px; width: 310px; top: 976px;
    text-align: center; font-size: 17px; line-height: 1.35; margin: 0;
  }
  .phone-bar {
    position: absolute; left: 0; top: 1032px; width: 328px; height: 48px;
    background: var(--brown); color: var(--white);
    font-size: 37px; font-weight: 600; letter-spacing: 1px;
    display: flex; align-items: center; justify-content: center;
  }
  .address {
    position: absolute; left: 20px; width: 310px; top: 1084px;
    text-align: center; font-size: 15px; line-height: 1.22; margin: 0;
  }
  .web-bar {
    position: absolute; left: 0; top: 1148px; width: 360px; height: 44px;
    background: var(--lime);
    display: flex; align-items: center; padding-left: 16px; box-sizing: border-box;
    font-size: 21px; font-weight: 700; color: var(--brown);
  }
</style>
</head>
<body>
<main class="page">
  <svg class="backdrop" width="848" height="1200" viewBox="0 0 848 1200" aria-hidden="true">
    <defs>
      <linearGradient id="roomTones" x1="0" y1="0" x2="1" y2="1">
        <stop offset="0" stop-color="#c79a5a"/>
        <stop offset="0.45" stop-color="#efe6cf"/>
        <stop offset="1" stop-color="#8f8576"/>
      </linearGradient>
    </defs>
    <path d="M0,0 H600 C520,150 320,270 0,344 Z" fill="var(--cream)"/>
    <path d="M600,0 H628 C560,200 360,330 0,424 V344 C320,270 520,150 600,0 Z" fill="var(--brown)"/>
    <path d="M848,650 C700,660 480,700 390,800 C372,830 368,900 368,1200 H848 Z" fill="var(--brown)"/>
    <path d="M848,680 C710,690 500,730 414,818 C398,845 395,900 395,1200 H848 Z" fill="url(#roomTones)" role="img" aria-label="Photograph of a bright consulting room with cream tub chairs, a wooden side table and a window"/>
  </svg>

  <div class="brand"><span class="brand-dot"></span>The Willowmere Talking Rooms House</div>

  <h1 class="script script--lead">The rooms are available to</h1>
  <div class="script script--hero">hire all day</div>
  <div class="script script--sub">into the evenings and at</div>
  <div class="script script--hero2">weekends</div>

  <div class="side-bar"></div>
  <div class="rooms-copy">
    <p>There are <strong>8 rooms</strong>, all suitable for <strong>Couples work, Individual Counselling</strong> or <strong>Supervision sessions.</strong></p>
    <p class="detail">Some rooms are designed to be used by <strong>physical therapists</strong> as well. One of them is large enough to use for <strong>Family Therapy</strong>, to hold groups or to run Training Sessions for approximately <strong>fourteen people</strong>.</p>
  </div>

  <p class="hours">Appointments available<br>throughout the day and evening</p>
  <div class="phone-bar">01632 960418</div>
  <p class="address">and 14 Mill Lane, Old Town,<br>Ashlake AK2 7RD.<br>rooms@hwrk-ashlake.co.uk</p>
  <div class="web-bar">www.hwrk-ashlake.co.uk</div>
</main>
</body>
</html>
```